Stationary and email footer design using existing Logo design

Using the Logo design I currently have I need now to have this applied to all stationary requirements including email footer, Letter Head and footer, envelopes both window and non window ( standard letter size ).
You previously did the Logo and business cards so that's good.

```html
<!DOCTYPE html>
<html lang="en">
<head>
<meta charset="utf-8">
<title>Lilac Ridge Financial Architects – Stationery Suite</title>
<link href="https://fonts.googleapis.com/css2?family=Cinzel:wght@600&family=Open+Sans:wght@400;600&family=Arimo&display=swap" rel="stylesheet">
<style>
  :root {
    --bg: #e6d9f2;
    --paper: #ffffff;
    --purple: #7b4fb0;
    --purple-light: #a27fce;
    --grey: #8c8c8c;
    --ink: #333333;
  }
  * { box-sizing: border-box; margin: 0; padding: 0; }
  html, body { width: 1200px; height: 900px; overflow: hidden; }
  body { background: var(--bg); position: relative; font-family: 'Open Sans', sans-serif; }

  .sheet { position: absolute; background: var(--paper); box-shadow: 0 6px 18px rgba(90,50,130,.18); overflow: hidden; }
  .wave { position: absolute; left: 0; bottom: 0; width: 100%; display: block; }

  .brand { display: flex; align-items: center; gap: 8px; }
  .brand-mark { width: 22px; height: 22px; background: var(--purple); flex: none; }
  .brand-name { font-family: 'Cinzel', serif; font-weight: 600; color: var(--purple); font-size: 22px; letter-spacing: .5px; }

  /* Letterhead */
  .letterhead { left: 50px; top: 146px; width: 430px; height: 608px; }
  .letterhead .brand { position: absolute; left: 28px; top: 34px; }
  .letterhead .edge { position: absolute; left: 0; top: 34px; width: 4px; height: 30px; background: var(--purple); }
  .letterhead .edge-r { position: absolute; right: 0; top: 24px; width: 4px; height: 30px; background: var(--purple); }
  .contact { position: absolute; right: 24px; top: 26px; font-size: 7.5px; line-height: 1.7; color: var(--purple); font-weight: 600; text-align: left; }
  .contact li { list-style: none; display: flex; gap: 4px; align-items: flex-start; }
  .contact svg { width: 8px; height: 8px; flex: none; margin-top: 2px; }
  .letter-body { position: absolute; left: 28px; right: 28px; top: 100px; font-family: 'Arimo', sans-serif; font-size: 9px; line-height: 1.5; color: var(--ink); }
  .letter-body p { margin-bottom: 12px; }
  .tagline { font-family: 'Cinzel', serif; font-weight: 600; color: var(--purple); font-size: 10px; letter-spacing: .5px; }
  .letterhead .tagline { position: absolute; right: 28px; bottom: 66px; }

  /* Envelopes */
  .envelope-front { left: 560px; top: 115px; width: 540px; height: 240px; }
  .envelope-front .brand { position: absolute; left: 24px; top: 26px; }
  .envelope-front .return { position: absolute; left: 24px; top: 60px; font-size: 7.5px; line-height: 1.5; color: var(--purple); font-weight: 600; }

  .envelope-back { left: 560px; top: 385px; width: 540px; height: 240px; }
  .flap { position: absolute; left: 0; top: 0; width: 100%; height: 150px; display: block; }
  .envelope-back .brand { position: absolute; left: 50%; bottom: 26px; transform: translateX(-50%); }
  .envelope-back .brand-name { font-size: 16px; }
  .envelope-back .brand-mark { width: 16px; height: 16px; }

  /* Email footer */
  .email-footer { left: 560px; top: 655px; width: 540px; height: 130px; background: #f1f1f1; }
  .email-footer .brand { position: absolute; left: 20px; top: 34px; }
  .email-footer .tagline { position: absolute; left: 190px; top: 20px; }
  .email-footer .details { position: absolute; left: 20px; top: 66px; font-size: 8.5px; line-height: 1.6; color: var(--purple); font-weight: 600; }
</style>
</head>
<body>

<section class="sheet letterhead" aria-label="Letterhead">
  <span class="edge"></span><span class="edge-r"></span>
  <div class="brand"><span class="brand-mark"></span><span class="brand-name">Lilac Ridge</span></div>
  <ul class="contact">
    <li><svg viewBox="0 0 10 10"><path d="M5 0a3.5 3.5 0 0 0-3.5 3.5C1.5 6 5 10 5 10s3.5-4 3.5-6.5A3.5 3.5 0 0 0 5 0z" fill="currentColor"/></svg><span>Suite 4, Level 2 Harbour Court<br>12 Wattle Lane, Northbay WA 6100</span></li>
    <li><svg viewBox="0 0 10 10"><path d="M2 0l2 2.5-1 1.5a6 6 0 0 0 3 3l1.5-1L10 8l-1.5 2C4 10 0 6 0 1.5z" fill="currentColor"/></svg><span>08 5550 1234</span></li>
    <li><svg viewBox="0 0 10 10"><rect x="0" y="2" width="10" height="7" fill="currentColor"/><path d="M0 2l5 4 5-4" stroke="#fff" fill="none"/></svg><span>sam.reed@lilacridge.com.au</span></li>
  </ul>
  <div class="letter-body">
    <p>Lorem Ipsum is simply dummy text of the printing and typesetting industry. Lorem Ipsum has been the industry's standard dummy text ever since the 1500s, when an unknown printer took a galley of type and scrambled it to make a type specimen book. It has survived not only five centuries, but also the leap into electronic typesetting, remaining essentially unchanged.</p>
    <p>It is a long established fact that a reader will be distracted by the readable content of a page when looking at its layout. The point of using Lorem Ipsum is that it has a more-or-less normal distribution of letters, as opposed to using 'Content here, content here', making it look like readable English.</p>
    <p>Contrary to popular belief, Lorem Ipsum is not simply random text. It has roots in a piece of classical Latin literature from 45 BC, making it over 2000 years old. Lorem Ipsum comes from sections 1.10.32 and 1.10.33 of "de Finibus Bonorum et Malorum". The generated Lorem Ipsum is therefore always free from repetition, injected humour, or non-characteristic words etc.</p>
  </div>
  <span class="tagline">Working with you to design your financial future</span>
  <svg class="wave" viewBox="0 0 430 70" preserveAspectRatio="none" height="70" aria-hidden="true">
    <path d="M0 70 L0 52 Q220 28 430 8 L430 70 Z" fill="var(--grey)"/>
    <path d="M0 50 Q220 22 430 0 L430 8 Q220 30 0 56 Z" fill="var(--purple)"/>
    <path d="M0 48 Q220 16 430 -4" stroke="var(--purple-light)" stroke-width="1.2" fill="none"/>
  </svg>
</section>

<section class="sheet envelope-front" aria-label="Envelope front">
  <div class="brand"><span class="brand-mark"></span><span class="brand-name">Lilac Ridge</span></div>
  <p class="return">Suite 4, Level 2 Harbour Court 12 Wattle Lane,<br>Northbay WA 6100</p>
  <svg class="wave" viewBox="0 0 540 60" preserveAspectRatio="none" height="60" aria-hidden="true">
    <path d="M0 60 L0 40 Q280 26 540 4 L540 60 Z" fill="var(--grey)"/>
    <path d="M0 38 Q280 16 540 0 L540 6 Q280 28 0 44 Z" fill="var(--purple)"/>
    <path d="M0 36 Q280 10 540 -4" stroke="var(--purple-light)" stroke-width="1" fill="none"/>
  </svg>
</section>

<section class="sheet envelope-back" aria-label="Envelope back">
  <svg class="flap" viewBox="0 0 540 150" preserveAspectRatio="none" aria-hidden="true">
    <path d="M0 0 L540 0 L540 30 Q500 40 470 52 L60 135 Q30 142 18 120 L0 80 Z" fill="#fafafa" stroke="#e2e2e2"/>
  </svg>
  <div class="brand"><span class="brand-mark"></span><span class="brand-name">Lilac Ridge</span></div>
</section>

<section class="sheet email-footer" aria-label="Email footer">
  <span class="tagline">Working with you to design your financial future</span>
  <div class="brand"><span class="brand-mark"></span><span class="brand-name">Lilac Ridge</span></div>
  <p class="details">Suite 4, Level 2 Harbour Court 12 Wattle Lane, Northbay WA 6100<br>08 5550 1234 &nbsp;|&nbsp; sam.reed@lilacridge.com.au</p>
  <svg class="wave" viewBox="0 0 540 40" preserveAspectRatio="none" height="40" aria-hidden="true">
    <path d="M0 40 L0 26 Q280 18 540 2 L540 40 Z" fill="var(--grey)"/>
    <path d="M0 24 Q280 10 540 -2 L540 4 Q280 20 0 28 Z" fill="var(--purple)"/>
  </svg>
</section>

</body>
</html>
```